Website Design for new skincare product launch/rebranding

The Dew Meridian website is currently live and built through Pagevolt.com. While the existing site has served as a strong starting point, I’m now looking to elevate the overall experience with a complete redesign that reflects the growth and vision of the brand. This will be a full visual and functional revamp — not just a refresh — with the goal of creating a more elevated, intuitive, and conversion-focused platform. I’m looking for a designer who can not only reimagine the layout and visuals, but also collaborate on optimizing the user journey and site structure for both storytelling and sales.

Target Market(s)

Age 25- 45 (core), with secondary appeal to 18-55. Primarily women, but gender inclusive. Wellness/Holistic Beauty/Organic Ingredients, Botanical.

Industry/Entity Type

Beauty, aesthetics, wellness.

Number of Pages Required

5+ page

Font styles to use
Other font styles liked:
• Gravesned Sans Family

Colors

Designer to choose colors to be used in the design.

Requirements
Must have
• Include standard pages (Home, Our Story/Values, Shop, Product Detail with ingredients/description/etc., Contact) and any other recommended sections to optimize conversion. Minimal, clean, calming visual. Seamlessly integrate with Cartwell for all product sales.
Nice to have
• Company colors are attached in images, along with first two products that are launching. One called Velunmist, and one called Petravelle. Fonts and shapes need to align accordingly. Feel elevated, neutral, and luxe while maintaining a grounded, earthy minimalism. Visual inspiration includes brands like Lantern Grove, Marble Osprey, and TOvelin — minimal yet high-end, with thoughtful use of whitespace, typography, and subtle movement. Would LOVE to have movement (short clip GIF) on either the home page or ingredient page, reference TOvelin website (homepage or LuminWeave System™ Tab)
Should not have
• dark colors, complex design elements, too many different fonts. For ingredients, stick to botanical images and information only, with no mentions of CBD or use of leaf imagery.

```html
<!DOCTYPE html>
<html lang="en">
<head>
<meta charset="utf-8">
<title>Dew Meridian — Aligned Skincare</title>
<link href="https://fonts.googleapis.com/css2?family=Montserrat:wght@400;500;600&family=Bodoni+Moda:wght@500&display=swap" rel="stylesheet">
<style>
:root{
  --ink:#2b2a29;
  --ink-soft:#5a5754;
  --muted:#8f8b87;
  --line:#c9c5c1;
  --paper:#ffffff;
  --panel:#ececeb;
  --sand:#d9d2cd;
  --stone:#8c8983;
  --mist:#eee9e5;
  --ghost:#ece5e0;
}
*{box-sizing:border-box;margin:0;padding:0}
html,body{width:1200px;height:4640px;overflow:hidden}
body{position:relative;background:var(--paper);font-family:"Montserrat",sans-serif;color:var(--ink)}
.abs{position:absolute}
.btn{position:absolute;display:flex;align-items:center;justify-content:center;border-radius:40px;font-size:10px;font-weight:600;letter-spacing:.06em;text-transform:uppercase}
.btn-dark{background:var(--ink);color:#fff}
.btn-line{border:1.5px solid var(--line);color:var(--muted);background:transparent}
.display{font-weight:500;text-transform:uppercase;letter-spacing:.04em;line-height:1.2}

/* nav */
.nav{left:112px;top:29px;width:976px;height:56px;background:#fff;border-radius:10px;box-shadow:0 4px 18px rgba(0,0,0,.08);display:flex;align-items:center;padding:0 38px;font-size:11px;color:var(--ink-soft)}
.nav-links{display:flex;gap:28px}
.brand{position:absolute;left:50%;transform:translateX(-50%);font-family:"Bodoni Moda",serif;font-size:26px;color:var(--line)}
.nav-tools{margin-left:auto;display:flex;align-items:center;gap:26px}
.search{width:144px;height:34px;border:1.5px solid var(--line);border-radius:20px;display:flex;align-items:center;justify-content:space-between;padding:0 4px 0 16px;color:var(--muted);font-size:10px}
.search span.dot{width:26px;height:26px;border-radius:50%;background:var(--muted)}
.tool{display:flex;align-items:center;gap:8px;color:var(--muted);font-size:10px}
.tool i{width:26px;height:26px;border:1.5px solid var(--line);border-radius:50%;display:block}

/* hero */
.hero{left:0;top:0;width:1200px;height:685px;background:linear-gradient(100deg,#6f6864 0%,#8d8580 38%,#bdb4ad 62%,#9c948f 100%)}
.hero-title{left:112px;top:158px;color:#fff;font-size:46px}
.hero-sub{left:112px;top:347px;color:#fff;font-size:14px}

/* why */
.card{position:absolute;border-radius:10px;display:flex;flex-direction:column;align-items:center;text-align:center;padding:0 22px;box-shadow:0 10px 30px rgba(0,0,0,.1)}
.card .icon{width:84px;height:84px;border-radius:50%;background:#fff;display:flex;align-items:center;justify-content:center;margin-top:26px}
.card h3{font-size:13px;font-weight:500;letter-spacing:.03em;margin-top:22px;text-transform:uppercase}
.card p{font-size:10px;line-height:1.35;margin-top:8px}
.card-sand{background:var(--sand);color:var(--ink)}
.card-sand p{color:var(--ink-soft)}
.card-stone{background:var(--stone);color:#fff}
.card-dark{background:var(--ink);color:#fff}
.card-light{background:linear-gradient(180deg,#f1f1f0,#e2e2e1);color:var(--ink)}
.card-light p{color:var(--ink-soft)}
.photo{position:absolute;border-radius:8px;box-shadow:0 10px 30px rgba(0,0,0,.12)}
.why-title{left:400px;top:1100px;width:400px;text-align:center;font-size:36px}
.why-sub{left:400px;top:1198px;width:400px;text-align:center;font-size:11px;color:var(--ink-soft);line-height:1.5}

/* products */
.panel{left:25px;top:1667px;width:1150px;height:558px;background:var(--panel);border-radius:36px}
.prod-title{left:112px;top:1724px;font-size:33px}
.tab{height:36px;top:1744px}
.prod-img{position:absolute;top:1845px;width:316px;height:240px;border-radius:8px}
.prod-name{position:absolute;top:2103px;font-size:13px;font-weight:500;text-transform:uppercase}
.prod-price{position:absolute;top:2126px;font-size:11px;color:var(--muted)}
.prod-price s{margin-left:2px}
.prod-add{position:absolute;top:2151px;font-size:10px;font-weight:600;text-decoration:underline}

/* savings */
.save-title{left:112px;top:2300px;font-size:36px}
.save-copy{left:753px;top:2306px;width:325px;font-size:11px;line-height:1.5;color:var(--ink-soft)}
.ghost-word{font-family:"Bodoni Moda",serif;color:var(--ghost);font-size:158px;line-height:1;white-space:nowrap;left:-10px;width:1220px;text-align:center;letter-spacing:-.02em}

/* testimonials */
.quote-title{left:0;top:2955px;width:1200px;text-align:center;font-size:34px}
.quote-sub{left:290px;top:3020px;width:620px;text-align:center;font-size:11px;line-height:1.55;color:var(--ink-soft)}
.slider-band{left:0;top:3135px;width:1200px;height:227px;background:#f1f1f0}
.quote-card{left:258px;top:3101px;width:684px;height:297px;background:#8b8480;border-radius:4px;box-shadow:0 14px 34px rgba(0,0,0,.18)}
.quote-inner{left:528px;top:3113px;width:398px;height:271px;background:#fff;border-radius:6px;padding:30px 40px}
.quote-inner h4{font-size:14px;font-weight:600}
.quote-inner .role{font-size:10px;color:var(--muted);margin-top:6px}
.quote-inner p{font-size:10.5px;line-height:1.8;color:var(--ink-soft);margin-top:30px}
.quote-inner .date{font-size:10px;color:var(--ink-soft);margin-top:24px}
.qmark{font-family:"Bodoni Moda",serif;font-size:90px;line-height:1;color:#bdb9b5}

/* newsletter */
.join{left:0;top:3486px;width:1200px;height:631px;background:linear-gradient(100deg,#a79d94 0%,#8a7f77 45%,#6d635c 70%,#9a9087 100%)}
.join-title{left:112px;top:3618px;color:#fff;font-size:34px}
.join-copy{left:112px;top:3720px;width:290px;color:#fff;font-size:11px;line-height:1.45}
.email{left:753px;top:3657px;width:334px;height:37px;border:1.5px solid rgba(255,255,255,.8);border-radius:20px;color:#fff;font-size:10px;display:flex;align-items:center;padding-left:30px}

/* footer */
.foot-col{position:absolute;top:4225px;font-size:10px;color:var(--ink-soft);line-height:2.2}
.foot-col h5{font-size:11px;font-weight:600;color:var(--ink);letter-spacing:.03em;margin-bottom:2px}
.foot-div{position:absolute;top:4195px;width:1.5px;height:165px;background:var(--line)}
.bar{left:112px;top:4553px;width:975px;height:54px;background:var(--ink);border-radius:8px;color:#fff;font-size:10px;display:flex;align-items:center;padding:0 64px}
.socials{margin-left:auto;display:flex;gap:12px}
.socials i{width:26px;height:26px;border-radius:50%;background:#fff;display:block}
</style>
</head>
<body>

<!-- Hero -->
<div class="abs hero" role="img" aria-label="Woman in a white bathrobe applying under-eye patches in a bright bathroom"></div>
<nav class="abs nav">
  <div class="nav-links"><span>About</span><span>Why Choose Us</span><span>Products</span><span>Testimonials</span></div>
  <div class="brand">Dew Meridian</div>
  <div class="nav-tools">
    <div class="search">Search<span class="dot"></span></div>
    <div class="tool"><i></i>Account</div>
    <div class="tool"><i></i>Cart (0)</div>
  </div>
</nav>
<h1 class="abs display hero-title">Aligned Skincare<br>for Hydrated,<br>Balanced Skin</h1>
<p class="abs hero-sub">Short 1–2 sentence brand promise</p>
<a class="btn btn-dark" style="left:112px;top:384px;width:140px;height:39px">Shop Now</a>
<a class="btn btn-line" style="left:268px;top:384px;width:197px;height:39px;color:#fff;border-color:rgba(255,255,255,.8)">Discover Our Story</a>

<!-- Why choose -->
<svg width="0" height="0" style="position:absolute">
  <symbol id="lotus" viewBox="0 0 40 24"><g fill="none" stroke="#8c8983" stroke-width="1.3"><path d="M20 22 C14 16 14 8 20 2 C26 8 26 16 20 22Z"/><path d="M20 22 C12 20 8 14 9 8 C15 10 18 15 20 22Z"/><path d="M20 22 C28 20 32 14 31 8 C25 10 22 15 20 22Z"/><path d="M20 22 C10 23 4 19 2 14 C9 13 15 17 20 22Z"/><path d="M20 22 C30 23 36 19 38 14 C31 13 25 17 20 22Z"/></g></symbol>
</svg>

<div class="card card-sand" style="left:258px;top:787px;width:248px;height:226px">
  <div class="icon"><svg width="44" height="28"><use href="#lotus"/></svg></div>
  <h3>Hydration at the Core</h3>
  <p>Lorem ipsum dolor sit amet, consectetur adipiscing elit, sed do eiusmod tempor incididunt.</p>
</div>
<div class="photo" style="left:609px;top:771px;width:295px;height:215px;background:linear-gradient(135deg,#d9c7bb,#b79c8c)" role="img" aria-label="Woman with a clay face mask holding cucumber slices"></div>

<div class="card card-stone" style="left:113px;top:1083px;width:249px;height:225px">
  <div class="icon"><svg width="44" height="28"><use href="#lotus"/></svg></div>
  <h3>Botanical Purity</h3>
  <p>Lorem ipsum dolor sit amet, consectetur adipiscing elit, sed do eiusmod tempor incididunt.</p>
</div>

<h2 class="abs display why-title">Why Choose<br>Dew Meridian</h2>
<p class="abs why-sub">Elevated skincare, rooted in nature and guided by science —<br>for skin that feels balanced, hydrated, and alive.</p>
<a class="btn btn-dark" style="left:517px;top:1243px;width:166px;height:38px">Learn More</a>

<div class="card card-dark" style="left:836px;top:1047px;width:250px;height:225px">
  <div class="icon"><svg width="44" height="28"><use href="#lotus"/></svg></div>
  <h3>Sustainable &amp; Mindful</h3>
  <p>Lorem ipsum dolor sit amet, consectetur adipiscing elit, sed do eiusmod tempor incididunt.</p>
</div>

<div class="photo" style="left:258px;top:1377px;width:315px;height:203px;background:linear-gradient(135deg,#8a7566,#5e6a78)" role="img" aria-label="Woman with a towel wrap touching her cheek, eyes closed"></div>

<div class="card card-light" style="left:681px;top:1331px;width:252px;height:228px">
  <div class="icon"><svg width="44" height="28"><use href="#lotus"/></svg></div>
  <h3>Skin-Centric Simplicity</h3>
  <p>Lorem ipsum dolor sit amet, consectetur adipiscing elit, sed do eiusmod tempor incididunt.</p>
</div>

<!-- Products -->
<div class="abs panel"></div>
<h2 class="abs display prod-title">Our Products<br>Whit Best Quality</h2>
<a class="btn btn-dark tab" style="left:649px;width:137px">New Arrivals</a>
<a class="btn btn-line tab" style="left:798px;width:137px">Bestsellers</a>
<a class="btn btn-line tab" style="left:950px;width:137px">Sale</a>

<svg class="abs" style="left:52px;top:1958px" width="34" height="16" viewBox="0 0 34 16"><path d="M33 8H2M9 1 2 8l7 7" fill="none" stroke="#2b2a29" stroke-width="1.5"/></svg>
<svg class="abs" style="left:1112px;top:1958px" width="34" height="16" viewBox="0 0 34 16"><path d="M1 8h31M25 1l7 7-7 7" fill="none" stroke="#8f8b87" stroke-width="1.5"/></svg>

<div class="prod-img" style="left:112px;background:linear-gradient(180deg,#f7f7f7,#e4e4e4)" role="img" aria-label="Two white balm tubes"></div>
<div class="prod-img" style="left:441px;background:linear-gradient(135deg,#d8cfc8,#a8a29d)" role="img" aria-label="Facial treatment with a brush applying mask"></div>
<div class="prod-img" style="left:771px;background:linear-gradient(135deg,#e6e3e0,#bfb6ae)" role="img" aria-label="Woman in a towel wrap with cucumber slices on her eyes"></div>

<div class="prod-name" style="left:112px">Serene Dune</div>
<div class="prod-price" style="left:112px">4,500.00zł</div>
<div class="prod-add" style="left:112px">Add To Cart</div>
<div class="prod-name" style="left:441px">Velvet Tide Mist</div>
<div class="prod-price" style="left:441px">3,999.00zł <s>5,000.00zł</s></div>
<div class="prod-add" style="left:441px">Add To Cart</div>
<div class="prod-name" style="left:771px">Amber Quill</div>
<div class="prod-price" style="left:771px">4,500.00zł</div>
<div class="prod-add" style="left:771px">Add To Cart</div>

<!-- Savings -->
<h2 class="abs display save-title">Exclusive Savings<br>on Dew Meridian<br>Favorites</h2>
<p class="abs save-copy">Lorem ipsum dolor sit amet, consectetur adipiscing elit, sed do eiusmod tempor incididunt ut labore et dolore magna aliqua. Quis ipsum suspendisse ultrices gravida. Risus commodo viverra maecenas accumsan lacus vel facilisis.</p>
<div class="abs ghost-word" style="top:2498px">DEW MERIDIAN</div>
<div class="abs" style="left:492px;top:2337px;width:214px;height:541px;border-radius:60px 60px 14px 14px;background:linear-gradient(90deg,#b9b8b7,#e2e2e1 45%,#c7c6c5)" role="img" aria-label="Velunmist botanical serum dropper bottle"></div>
<a class="btn btn-dark" style="left:113px;top:2740px;width:137px;height:38px">Add To Cart</a>
<a class="btn btn-line" style="left:263px;top:2740px;width:137px;height:38px">Shop Now</a>
<svg class="abs" style="left:995px;top:2751px" width="34" height="16" viewBox="0 0 34 16"><path d="M33 8H2M9 1 2 8l7 7" fill="none" stroke="#2b2a29" stroke-width="1.5"/></svg>
<svg class="abs" style="left:1052px;top:2751px" width="34" height="16" viewBox="0 0 34 16"><path d="M1 8h31M25 1l7 7-7 7" fill="none" stroke="#8f8b87" stroke-width="1.5"/></svg>

<!-- Testimonials -->
<h2 class="abs display quote-title">What Our Clients Say</h2>
<p class="abs quote-sub">Lorem ipsum dolor sit amet, consectetur adipiscing elit, sed do eiusmod tempor incididunt ut labore et dolore magna aliqua. Quis ipsum suspendisse ultrices gravida. Risus commodo viverra maecenas accumsan lacus vel facilisis.</p>
<div class="abs slider-band"></div>
<p class="abs" style="left:0;top:3210px;width:250px;font-size:10px;line-height:1.8;color:#bdb9b5">adipiscing elit, sed do eiusmod tempor<br>a. Quis ipsum suspendisse ultrices gravida.<br>an lacus vel facilisis.</p>
<div class="abs qmark" style="left:208px;top:3150px">”</div>
<div class="abs" style="left:940px;top:3150px;width:50px;height:50px;border-radius:50%;background:#d8d3cf" role="img" aria-label="Client portrait"></div>
<div class="abs" style="left:1008px;top:3166px;font-size:14px;font-weight:600;color:#a5a19d">THEO P.</div>
<div class="abs" style="left:1008px;top:3188px;font-size:10px;color:#c4c0bc">Designer</div>
<p class="abs" style="left:940px;top:3225px;width:270px;font-size:10px;line-height:1.8;color:#bdb9b5;white-space:nowrap">em ipsum dolor sit amet, consectetur adipi<br>ididunt ut labore et dolore magna aliqua. Q<br>us commodo viverra maecenas accumsan l</p>
<div class="abs" style="left:940px;top:3318px;font-size:10px;color:#a5a19d">May 2025 6:30 am</div>

<div class="abs quote-card"></div>
<div class="abs" style="left:258px;top:3101px;width:252px;height:297px;background:linear-gradient(135deg,#e8e2dd,#b9aca2)" role="img" aria-label="Smiling woman with foam cleanser on her face"></div>
<div class="abs quote-inner">
  <div class="abs qmark" style="right:30px;top:18px;color:#8f8b87">”</div>
  <h4>NOLAN B.</h4>
  <div class="role">Designer</div>
  <p>Lorem ipsum dolor sit amet, consectetur adipiscing elit, sed do eiusmod tempor incididunt ut labore et dolore magna aliqua. Quis ipsum suspendisse ultrices gravida. Risus commodo viverra maecenas accumsan lacus vel facilisis.</p>
  <div class="date">15 May 2025 6:30 am</div>
</div>

<!-- Newsletter -->
<div class="abs join" role="img" aria-label="Woman in a towel holding a jar of cream in a warm bedroom"></div>
<h2 class="abs display join-title">Join the<br>Aligned List</h2>
<p class="abs join-copy">Be the first to discover new launches, exclusive offers, and skincare rituals that keep your skin in perfect balance.</p>
<div class="abs email">Enter Email</div>
<a class="btn btn-dark" style="left:753px;top:3703px;width:137px;height:34px">Subscribe</a>

<!-- Footer -->
<div class="foot-col" style="left:113px"><h5>QUICK LINKS</h5>About<br>Products<br>Testimonials<br>Contact</div>
<div class="foot-div" style="left:379px"></div>
<div class="foot-col" style="left:514px"><h5>MY ACCOUNT</h5>Login<br>Order History<br>Newsletter<br>Returns</div>
<div class="foot-div" style="left:779px"></div>
<div class="foot-col" style="left:915px"><h5>CUSTOMER SERVICE</h5>Contact Us<br>Store Locations<br>Site Map<br>Delivery Information</div>
<div class="abs ghost-word" style="top:4392px;font-size:170px">DEW MERIDIAN</div>
<div class="abs bar">
  <span>Copyright © 2025. All rights reserved.</span>
  <div class="socials"><i aria-label="Social link"></i><i aria-label="Social link"></i><i aria-label="Social link"></i><i aria-label="Social link"></i></div>
</div>

</body>
</html>
```